Kito Rise and Glow Dance Fitness-KRGDF

Catchy POSTER .
The poster must attract both eyes of all ages looking for fitness,Ritmoflex to have fun, professional dance training and Yoga.

Target Market(s)

Dancers and Non Dancers

Industry/Entity Type

Training

Requirements
Must have
• Kito Dance Ensemble
Presents
KITO RISE AND GLOW DANCE FITNESS

African Dance
Modern/Samtidsdans,
Yoga
Ritmoflex
Hip Hop
Massage and repertoire classes.

Venue:Vetlefjord Kulturhus
Call 47351208 to register/TEXT
kitoarts@kitomail.example
www.kitoarts-example.org
Nice to have
• OG creativity...think outside the box
Should not have
• Please NO cartoon charectors!!! or BALLET DANCING LIONS!!!

```html
<!DOCTYPE html>
<html lang="en">
<head>
<meta charset="utf-8">
<title>Kito Rise and Glow Dance Fitness</title>
<link rel="stylesheet" href="https://fonts.googleapis.com/css2?family=Anton&family=Roboto+Condensed:wght@400;700&display=swap">
<style>
  :root {
    --night: #1b1f5c;
    --violet: #5a3f9e;
    --glow: #c9d4ff;
    --white: #ffffff;
    --gold: #ffe23a;
    --amber: #ff9a1a;
    --red: #e11b22;
    --orange: #f26a1b;
    --green: #3aa935;
    --blue: #1f7ad1;
    --leaf: #2fae4a;
    --pink: #e8487c;
    --outline: #14123a;
  }
  * { margin: 0; padding: 0; box-sizing: border-box; }
  html, body { width: 900px; height: 1200px; overflow: hidden; background: var(--night); }
  .poster {
    position: relative; width: 900px; height: 1200px; overflow: hidden;
    font-family: "Roboto Condensed", Arial, sans-serif; color: var(--white);
    background: radial-gradient(ellipse at 45% 40%, var(--glow) 0%, #8f86d6 22%, var(--violet) 45%, var(--night) 80%);
  }
  .dancer-photo {
    position: absolute; left: 40px; top: 270px; width: 520px; height: 860px;
    background: radial-gradient(ellipse at 50% 45%, rgba(120,150,200,.75) 0%, rgba(60,90,150,.55) 45%, rgba(40,50,110,0) 75%);
  }
  .presents { position: absolute; top: 18px; width: 100%; text-align: center; font-size: 24px; font-weight: 700; letter-spacing: 1px; }
  .title-line {
    position: absolute; top: 56px; width: 100%; text-align: center;
    font-family: "Anton", Impact, sans-serif; font-size: 54px; letter-spacing: 1px;
    -webkit-text-stroke: 3px var(--outline); paint-order: stroke fill;
  }
  .title-main {
    position: absolute; top: 118px; width: 100%; text-align: center;
    font-family: "Anton", Impact, sans-serif; font-size: 98px; line-height: 1.05; letter-spacing: 2px;
    color: var(--gold); -webkit-text-stroke: 4px var(--outline); paint-order: stroke fill;
    text-shadow: 0 4px 0 var(--amber);
  }
  .audience { position: absolute; top: 236px; width: 100%; text-align: center; font-size: 42px; font-weight: 700; }
  .classes-heading {
    position: absolute; top: 330px; right: 30px; font-family: "Anton", Impact, sans-serif;
    font-size: 82px; letter-spacing: 2px; -webkit-text-stroke: 3px var(--outline); paint-order: stroke fill;
  }
  .class-bar {
    position: absolute; right: 30px; height: 52px; display: flex; align-items: center; justify-content: center;
    font-size: 34px; font-weight: 400; padding: 0 14px;
  }
  .class-bar.african { top: 432px; width: 300px; background: var(--red); }
  .class-bar.modern { top: 496px; width: 420px; background: var(--orange); }
  .class-bar.yoga { top: 560px; width: 195px; background: var(--green); }
  .class-bar.ritmoflex { top: 624px; width: 240px; background: var(--blue); }
  .class-bar.hiphop { top: 688px; width: 255px; background: var(--leaf); }
  .class-bar.massage { top: 752px; width: 435px; background: var(--pink); }
  .venue { position: absolute; top: 860px; left: 220px; font-size: 44px; font-weight: 700; }
  .call {
    position: absolute; top: 920px; width: 100%; text-align: center;
    font-family: "Anton", Impact, sans-serif; font-size: 64px; color: var(--gold);
    -webkit-text-stroke: 5px var(--red); paint-order: stroke fill;
  }
  .coproduced { position: absolute; top: 1010px; width: 100%; text-align: center; font-size: 28px; }
  .contact {
    position: absolute; top: 1100px; height: 72px; display: flex; align-items: center; justify-content: center;
    font-size: 28px; font-weight: 700;
  }
  .contact.email { left: 25px; width: 420px; background: var(--red); }
  .contact.web { right: 25px; width: 410px; background: var(--blue); }
</style>
</head>
<body>
<div class="poster">
  <div class="dancer-photo" role="img" aria-label="Photo of a woman in jeans and a cropped top dancing mid-move in front of light rays"></div>

  <p class="presents">K.D.E presents</p>
  <h1 class="title-line">KITO RISE AND GLOW</h1>
  <p class="title-main">DANCE FITNESS</p>
  <p class="audience">for ADULTS</p>

  <h2 class="classes-heading">CLASSES</h2>
  <div class="class-bar african">African Dance</div>
  <div class="class-bar modern">Modern/Samtidsdans</div>
  <div class="class-bar yoga">Yoga</div>
  <div class="class-bar ritmoflex">Ritmoflex</div>
  <div class="class-bar hiphop">Hip Hop</div>
  <div class="class-bar massage">Massage and repertoire</div>

  <p class="venue">Venue:Vetlefjord Kulturhus</p>
  <p class="call">CALL 47351208 TO REGISTER</p>
  <p class="coproduced">Co-produced by Vetlefjord Kulturhus</p>

  <div class="contact email">kitoarts@kitomail.example</div>
  <div class="contact web">www.kitoarts-example.org</div>
</div>
</body>
</html>
```